Brochure Design Project

Architectural photography and virtual tour provider for local and national real estate markets. You can use my website for design and image needs. www.larchviewhomeshots.com

```html
<!DOCTYPE html>
<html lang="en">
<head>
<meta charset="utf-8">
<title>Larchview Home Shots – Tri-fold Brochure</title>
<link rel="stylesheet" href="https://fonts.googleapis.com/css2?family=Open+Sans:wght@400;600;700&display=swap">
<style>
:root{
  --page:#e4e4e4;
  --paper:#ffffff;
  --charcoal:#363638;
  --slate:#55767a;
  --slate-light:#dfe7e8;
  --ink:#3c3c3c;
  --muted:#6d6d6d;
  --on-dark:#e9e9e9;
  --photo-warm:linear-gradient(160deg,#c9a77c 0%,#8a6a4c 45%,#3f4b5a 100%);
  --photo-estate:linear-gradient(180deg,#f2efe8 0%,#cdb99a 35%,#7c6d58 55%,#4f7a3a 75%,#3e6a2c 100%);
  --photo-room:linear-gradient(165deg,#efe7d8 0%,#bfa98a 50%,#6d5a45 100%);
  --photo-living:linear-gradient(180deg,#ded8cf 0%,#9c948a 50%,#4a4540 100%);
  --photo-kitchen:linear-gradient(170deg,#d8dde0 0%,#8e979c 50%,#3b4348 100%);
}
*{box-sizing:border-box;margin:0;padding:0}
html,body{width:1200px;height:2402px;overflow:hidden}
body{background:var(--page);font-family:"Open Sans",Arial,sans-serif;color:var(--ink);position:relative}
.spread{position:absolute;left:40px;width:1120px;height:866px;display:flex;box-shadow:0 6px 24px rgba(0,0,0,.18);background:var(--paper)}
.spread--outside{top:223px}
.spread--inside{top:1312px}
.panel{position:relative;width:373.33px;height:100%;overflow:hidden;background:var(--paper)}
.panel--dark{background:var(--charcoal);color:var(--on-dark)}
.photo{position:absolute;left:0;width:100%}
.footer-band{position:absolute;left:0;right:0;bottom:0;height:40px;display:flex;align-items:center;gap:8px;padding:0 24px;font-size:12px;font-weight:600}
.footer-band--light{background:var(--slate-light);color:var(--slate)}
.footer-band--slate{background:var(--slate);color:#fff;justify-content:flex-end}
.globe{width:14px;height:14px}
.brand{display:flex;align-items:center;gap:10px}
.brand__mark{width:22px;height:22px;background:var(--slate)}
.brand__name{font-size:22px;font-weight:600}
.tagline{font-size:11px;font-style:normal;color:var(--muted)}
/* outside: about */
.about__band{position:absolute;top:232px;left:0;right:0;height:8px;background:var(--slate)}
.about__thumbs{position:absolute;top:256px;left:24px;display:flex;gap:14px}
.about__thumb{width:72px;height:72px;border-radius:50%;border:4px solid #fff;box-shadow:0 0 0 2px var(--slate)}
.about__title{position:absolute;top:352px;left:28px;font-size:24px;font-weight:600;color:var(--charcoal);padding-bottom:4px;border-bottom:3px solid var(--slate)}
.about__list{position:absolute;top:404px;left:28px;right:28px;list-style:none}
.about__list li{display:flex;gap:10px;margin-bottom:16px}
.about__list svg{flex:none;width:16px;height:16px;margin-top:2px}
.about__list strong{display:block;font-size:13px;color:var(--charcoal)}
.about__list span{font-size:11px;color:var(--muted);line-height:1.45}
/* outside: middle */
.middle__brand{position:absolute;top:60px;left:0;right:0;display:flex;flex-direction:column;align-items:center;gap:4px}
.middle__brand .brand__mark{background:var(--on-dark)}
.middle__brand .brand__name{color:#fff}
.middle__brand .tagline{color:#bdbdbd}
.quote{position:absolute;left:30px;right:30px;display:flex;gap:10px}
.quote__mark{font-size:40px;line-height:.9;color:var(--slate);font-weight:700}
.quote p{font-size:12px;line-height:1.5;color:#d7d7d7}
.quote cite{display:block;margin-top:8px;font-style:normal;font-size:12px;color:#bcbcbc}
.quote--one{top:190px}
.quote--two{top:330px}
.promo{position:absolute;top:470px;left:36px;right:36px;border:2px solid var(--slate);padding:14px 10px;text-align:center}
.promo__big{font-size:22px;font-weight:700;color:#fff}
.promo__small{font-size:18px;color:#e2e2e2;letter-spacing:.5px}
.contact{position:absolute;top:600px;left:0;right:0;text-align:center}
.contact h3{font-size:20px;font-weight:700;color:var(--slate);margin-bottom:18px;letter-spacing:.5px}
.contact p{font-size:13px;color:#dcdcdc;line-height:1.9}
/* outside: cover */
.cover__brand{position:absolute;top:48px;left:44px}
.cover__brand .brand__mark{width:40px;height:40px}
.cover__brand .brand__name{font-size:24px;color:var(--charcoal)}
.cover__headline{position:absolute;top:628px;left:28px;right:28px;font-size:19px;line-height:1.4;font-weight:600;text-transform:uppercase;color:var(--charcoal)}
/* inside */
.section-title{font-size:22px;font-weight:600;color:var(--charcoal)}
.best__box{position:absolute;top:318px;left:0;right:0;padding:16px 26px 0 30px;border-left:14px solid var(--slate)}
.best__box p{margin-top:12px;font-size:12px;line-height:1.6;color:var(--muted)}
.tours__title{position:absolute;top:34px;left:0;right:0;text-align:center;font-size:20px;font-weight:600;color:#fff}
.tours__grid{position:absolute;top:96px;left:24px;right:24px;display:grid;grid-template-columns:1fr 1fr;row-gap:28px}
.feature{display:flex;flex-direction:column;align-items:center;text-align:center;gap:8px}
.feature__icon{width:48px;height:48px;border-radius:8px;background:#4a4a4d;display:flex;align-items:center;justify-content:center}
.feature__icon svg{width:26px;height:26px}
.feature span{font-size:11px;line-height:1.35;color:#dedede;max-width:130px}
.how__title{position:absolute;top:34px;left:28px;font-size:22px;font-weight:700;color:var(--charcoal);text-transform:uppercase}
.how__text{position:absolute;top:80px;left:28px;right:28px}
.how__text p{font-size:12px;line-height:1.6;color:var(--muted);margin-bottom:12px}
.how__circle{position:absolute;top:430px;right:26px;width:110px;height:110px;border-radius:50%;border:5px solid #fff;box-shadow:0 0 0 2px var(--slate)}
.tech__box{position:absolute;top:560px;left:0;right:0;padding:6px 26px 0 30px;border-left:14px solid var(--slate)}
.tech__box .section-title{text-transform:uppercase;line-height:1.2}
.tech__box p{margin-top:10px;font-size:12px;line-height:1.6;color:var(--muted)}
</style>
</head>
<body>

<svg width="0" height="0" style="position:absolute">
  <symbol id="icon-globe" viewBox="0 0 16 16"><circle cx="8" cy="8" r="7" fill="none" stroke="currentColor" stroke-width="1.4"/><path d="M1 8h14M8 1c3 3 3 11 0 14M8 1c-3 3-3 11 0 14" fill="none" stroke="currentColor" stroke-width="1.2"/></symbol>
  <symbol id="icon-tick" viewBox="0 0 16 16"><circle cx="8" cy="8" r="8" fill="#55767a"/><path d="M4.5 8.3l2.3 2.3 4.7-4.9" fill="none" stroke="#fff" stroke-width="1.8"/></symbol>
</svg>

<!-- Outside spread -->
<section class="spread spread--outside">
  <article class="panel panel--about">
    <div class="photo" style="top:0;height:232px;background:var(--photo-warm)" role="img" aria-label="Photo of a furnished living room with large windows at dusk"></div>
    <div class="about__band"></div>
    <div class="about__thumbs">
      <div class="about__thumb" style="background:var(--photo-room)" role="img" aria-label="Round photo of a dining room"></div>
      <div class="about__thumb" style="background:var(--photo-kitchen)" role="img" aria-label="Round photo of a kitchen"></div>
      <div class="about__thumb" style="background:var(--photo-estate)" role="img" aria-label="Round aerial photo of a home"></div>
    </div>
    <h2 class="about__title">About us</h2>
    <ul class="about__list">
      <li><svg><use href="#icon-tick"/></svg><div><strong>30 Years Combined Experience</strong><span>Proudly serving home sellers and agents across the valley.</span></div></li>
      <li><svg><use href="#icon-tick"/></svg><div><strong>Professional Photos</strong><span>Bright, sharp images taken with pro gear and lighting.</span></div></li>
      <li><svg><use href="#icon-tick"/></svg><div><strong>Stunning Aerial Images</strong><span>Show the lot, the view and the whole neighborhood.</span></div></li>
    </ul>
    <div class="footer-band footer-band--light"><svg class="globe"><use href="#icon-globe"/></svg>www.larchviewhomeshots.com</div>
  </article>

  <article class="panel panel--dark">
    <div class="middle__brand">
      <div class="brand__mark"></div>
      <div class="brand__name">Larchview Home Shots</div>
      <div class="tagline">Become noticed</div>
    </div>
    <blockquote class="quote quote--one">
      <div class="quote__mark">&ldquo;</div>
      <div><p>I have been working with Larchview Home Shots for years. They are great to work with, fast turnaround time and great attention to detail.</p><cite>Marla Quinlan<br>Harborline Realty</cite></div>
    </blockquote>
    <blockquote class="quote quote--two">
      <div class="quote__mark">&ldquo;</div>
      <div><p>Best virtual tour provider in town. My listings and my sellers love the results!</p><cite>Tessa Morrow<br>Crestmark Properties</cite></div>
    </blockquote>
    <div class="promo">
      <div class="promo__big">Sell 32% Faster</div>
      <div class="promo__small">WIN MORE. SELL MORE.</div>
    </div>
    <div class="contact">
      <h3>CONTACT US</h3>
      <p>Formerly Desert Valley Home Tours<br>www.larchviewhomeshots.com<br>Call Now : (702) 555-0148</p>
    </div>
  </article>

  <article class="panel panel--cover">
    <div class="brand cover__brand">
      <div class="brand__mark"></div>
      <div><div class="brand__name">Larchview Home Shots</div><div class="tagline">Become noticed...</div></div>
    </div>
    <div class="photo" style="top:140px;height:470px;background:var(--photo-estate)" role="img" aria-label="Photo of a luxury home entrance with fountain and green lawn"></div>
    <h1 class="cover__headline">Architectural photography and virtual tour provider for local and national real estate markets.</h1>
    <div class="footer-band footer-band--slate"><svg class="globe"><use href="#icon-globe"/></svg>www.larchviewhomeshots.com</div>
  </article>
</section>

<!-- Inside spread -->
<section class="spread spread--inside">
  <article class="panel panel--best">
    <div class="photo" style="top:0;height:300px;background:var(--photo-room)" role="img" aria-label="Photo of a bright bedroom with wood floors"></div>
    <div class="best__box">
      <h2 class="section-title">What Makes Us The Best?</h2>
      <p>We bring the highest quality photography in a simple, elegant way. We'll handle making it look beautiful, so all you have to worry about is capturing more leads, winning more listings and selling more properties.</p>
    </div>
    <div class="photo" style="top:540px;height:326px;background:var(--photo-living)" role="img" aria-label="Photo of a living room with fireplace and white sofas"></div>
  </article>

  <article class="panel panel--dark">
    <h2 class="tours__title">All Photography Tours Include:</h2>
    <div class="tours__grid">
      <div class="feature"><div class="feature__icon"><svg viewBox="0 0 26 26"><rect x="3" y="8" width="20" height="13" rx="2" fill="none" stroke="#ddd" stroke-width="1.8"/><path d="M9 8l2-3h4l2 3" fill="none" stroke="#ddd" stroke-width="1.8"/><circle cx="13" cy="14.5" r="3.6" fill="none" stroke="#ddd" stroke-width="1.8"/></svg></div><span>High Quality Professional Photography</span></div>
      <div class="feature"><div class="feature__icon"><svg viewBox="0 0 26 26"><circle cx="13" cy="13" r="9" fill="none" stroke="#ddd" stroke-width="1.8"/><path d="M13 8v5l4 2" fill="none" stroke="#ddd" stroke-width="1.8"/></svg></div><span>1-2 Business Day Turnaround</span></div>
      <div class="feature"><div class="feature__icon"><svg viewBox="0 0 26 26"><path d="M6 13.5l4.5 4.5L20 8" fill="none" stroke="#ddd" stroke-width="2.2"/></svg></div><span>100% Satisfaction Guaranteed</span></div>
      <div class="feature"><div class="feature__icon"><svg viewBox="0 0 26 26"><path d="M4 13L13 5l9 8M7 11v10h12V11" fill="none" stroke="#ddd" stroke-width="1.8"/></svg></div><span>Professional Studio Editing</span></div>
      <div class="feature"><div class="feature__icon"><svg viewBox="0 0 26 26"><rect x="3" y="5" width="20" height="13" rx="1.5" fill="none" stroke="#ddd" stroke-width="1.8"/><path d="M9 22h8M13 18v4" stroke="#ddd" stroke-width="1.8"/></svg></div><span>Client Portal for 24 Hour Access</span></div>
      <div class="feature"><div class="feature__icon"><svg viewBox="0 0 26 26"><rect x="8" y="3" width="10" height="20" rx="2" fill="none" stroke="#ddd" stroke-width="1.8"/><circle cx="13" cy="19.5" r="1" fill="#ddd"/></svg></div><span>Mobile Friendly Online Gallery</span></div>
    </div>
    <div class="photo" style="top:540px;height:326px;background:var(--photo-living)" role="img" aria-label="Photo of an open living area with large windows"></div>
  </article>

  <article class="panel panel--how">
    <h2 class="how__title">How we do it</h2>
    <div class="how__text">
      <p>Our trained real estate photographers will capture all interior and exterior views, including area views of your property.</p>
      <p>We use only the best cameras and editing tools to produce results that make your property stand out and give buyers a sense of quality and attention to detail.</p>
    </div>
    <div class="photo" style="top:250px;height:250px;background:var(--photo-kitchen)" role="img" aria-label="Photo of a modern kitchen and dining room"></div>
    <div class="how__circle" style="background:var(--photo-room)" role="img" aria-label="Round photo of a sunlit room"></div>
    <div class="tech__box">
      <h2 class="section-title">TrueLight<br>Technology</h2>
      <p>Take your listings to the next level with our unique HDR TrueLight technology. Our editing process blends exposures for sharper photos, balanced colors and clear window views.</p>
    </div>
    <div class="footer-band footer-band--slate"><svg class="globe"><use href="#icon-globe"/></svg>www.larchviewhomeshots.com</div>
  </article>
</section>

</body>
</html>
```